Update Business Card Design Project

We've been in business nearly 15 years and about 10 years ago developed a brand that is now well recognized. The business card is boring, too much print and nothing that says 'We are WILLOWBY LANE' right off the mark.
We are a fun store, lots of new things on a regular basis. Especially in kitchen goods where the colours are strong and the emphasis is on pretty and practical. We like to have both!
Updates
Hi there,
Target Market(s)
Store customers and suppliers
Demographics aged 40-70yrs, mid to high income, mostly women or couples, rural setting but in the 'shopping district' of our region. 1 hour to nearest city.
Industry/Entity Type
Business
Requirements
Nice to have
- Incorporate the logo, if possible

```html
<!DOCTYPE html>
<html lang="en">
<head>
<meta charset="utf-8">
<title>Willowby Lane — Business Card</title>
<link rel="stylesheet" href="https://fonts.googleapis.com/css2?family=Michroma&display=swap">
<style>
  :root {
    --page-bg: #ececec;
    --card-bg: #e9e9e9;
    --ink-brown: #9c5418;
    --rule-gold: #d3a032;
    --mark-grey: #cdcdcd;
  }
  * { margin: 0; padding: 0; box-sizing: border-box; }
  html, body {
    width: 1200px;
    height: 1069px;
    overflow: hidden;
    background: var(--page-bg);
  }
  .canvas {
    position: relative;
    width: 1200px;
    height: 1069px;
  }
  .card {
    position: absolute;
    width: 425px;
    height: 245px;
    background: var(--card-bg);
  }
  .card--front { left: 72px; top: 440px; }
  .card--back  { left: 687px; top: 440px; }

  .brand {
    position: absolute;
    left: 0; right: 0;
    top: 30px;
    text-align: center;
    color: var(--ink-brown);
    font-family: "Michroma", sans-serif;
  }
  .brand__square {
    display: block;
    width: 44px;
    height: 44px;
    margin: 0 auto 10px;
    background: var(--ink-brown);
  }
  .brand__name {
    font-size: 17px;
    letter-spacing: 1px;
    line-height: 1.1;
  }
  .brand__tagline {
    font-size: 7px;
    letter-spacing: 0.5px;
    margin-top: 4px;
  }

  .contact {
    position: absolute;
    left: 0; right: 0;
    top: 156px;
    text-align: center;
    color: var(--ink-brown);
    font-family: "Michroma", sans-serif;
    font-size: 10px;
    line-height: 12px;
  }
  .contact__phones { margin-top: 6px; font-size: 11px; line-height: 15px; letter-spacing: 1px; }
  .contact__web { font-size: 11px; letter-spacing: 1px; }

  .note-area {
    position: absolute;
    inset: 0;
  }
</style>
</head>
<body>
<main class="canvas">
  <section class="card card--front" aria-label="Business card front">
    <div class="brand">
      <span class="brand__square" aria-hidden="true"></span>
      <div class="brand__name">Willowby Lane</div>
      <div class="brand__tagline">BED BATH &amp; HOME</div>
    </div>
    <address class="contact" style="font-style: normal;">
      <div class="contact__address">Harbour Gate Plaza, 4150 Orchard Street<br>Millbrook, Nova Scotia, B0P 2K7</div>
      <div class="contact__phones">1 800 555 0147<br>902 555 0147</div>
      <div class="contact__web">www.willowbylane.ca</div>
    </address>
  </section>

  <section class="card card--back" aria-label="Business card back with note lines">
    <svg class="note-area" width="425" height="245" viewBox="0 0 425 245">
      <rect class="note-area__mark" x="140" y="45" width="148" height="160" fill="var(--mark-grey)"/>
      <g class="note-area__rules" stroke="var(--rule-gold)" stroke-width="1.6">
        <line x1="38" y1="75" x2="386" y2="75"/>
        <line x1="38" y1="114" x2="386" y2="114"/>
        <line x1="38" y1="153" x2="386" y2="153"/>
        <line x1="38" y1="192" x2="386" y2="192"/>
      </g>
    </svg>
  </section>
</main>
</body>
</html>
```